Online medical reviews website needs banner advert!

We need banner advert templates for our website, www.traineepanel.net. These should meet the technical requirements of our partner (uploaded).

Our groundbreaking website allows doctors in training to rate and review their training.

The adverts should use the same modern design language and colour scheme as our website. They should use the text 'Help a junior doctor make a big decision - rate your training!'.

Vector assets should be supplied, allowing us to use alternative text in future.
Updates

Industry/Entity Type

Healthcare

Font styles to use
Other font styles liked:
• Karla

Colors
3277b5
0555a3
ffffff

Requirements
Must have
• Similar design to our website. Should be elegant & modern. Must allow future text to be easily inserted.
Should not have
• Unrelated design.

```html
<!DOCTYPE html>
<html lang="en">
<head>
<meta charset="utf-8">
<title>Rate your Training – Banner</title>
<link rel="stylesheet" href="https://fonts.googleapis.com/css2?family=Karla:wght@700;800&display=swap">
<style>
  :root {
    --blue-light: #2c56a6;
    --blue-deep: #264d98;
    --white: #ffffff;
    --button-text: #0d4f9e;
    --sky: #6f9fd6;
    --facade: #b9bec4;
    --facade-warm: #d9a53a;
  }
  html, body {
    margin: 0;
    padding: 0;
    overflow: hidden;
    background: var(--white);
  }
  .banner {
    position: relative;
    width: 1200px;
    height: 310px;
    overflow: hidden;
    font-family: "Karla", sans-serif;
  }
  .banner__backdrop {
    position: absolute;
    inset: 0;
    width: 654px;
    height: 310px;
  }
  .banner__photo {
    position: absolute;
    top: 0;
    left: 654px;
    width: 546px;
    height: 310px;
    background: linear-gradient(180deg, var(--sky) 0%, #9dbde3 22%, var(--facade) 34%, var(--facade-warm) 52%, var(--facade) 70%, #8d8b86 100%);
  }
  .banner__content {
    position: absolute;
    left: 48px;
    top: 82px;
  }
  .banner__headline {
    margin: 0;
    color: var(--white);
    font-weight: 800;
    font-size: 41px;
    line-height: 48px;
    letter-spacing: 0.5px;
    text-transform: uppercase;
    text-shadow: 0 2px 4px rgba(0, 0, 0, 0.35);
  }
  .banner__cta {
    display: inline-block;
    margin-top: 20px;
    padding: 0 18px;
    height: 48px;
    line-height: 48px;
    background: var(--white);
    color: var(--button-text);
    border-radius: 4px;
    font-weight: 700;
    font-size: 22px;
    text-decoration: none;
    box-shadow: 0 2px 5px rgba(0, 0, 0, 0.25);
  }
</style>
</head>
<body>
  <div class="banner">
    <svg class="banner__backdrop" viewBox="0 0 654 310" aria-hidden="true">
      <rect width="654" height="310" fill="var(--blue-light)"/>
      <polygon points="40,310 654,0 654,310" fill="var(--blue-deep)"/>
    </svg>

    <div class="banner__photo" role="img" aria-label="Photo of a modern hospital building with red, orange and yellow facade panels under a blue sky"></div>

    <div class="banner__content">
      <h1 class="banner__headline">Help a junior doctor<br>make a big decision -</h1>
      <a class="banner__cta" href="#">Rate your Training!</a>
    </div>
  </div>
</body>
</html>
```